Corvella Paintless Dent Removal

Our company works on vehicles removing dents using a highly skilled trade which the metal is massaged out with special tools without disturbing the original paint, hence paintless dent removal. Besides keeping the paint and metal original its also very environmentally friendly since no paint or toxic fillers are used. Also we we are one of the most experienced companies in the business with 25 years

Target Market(s)

Retail Automobile consumers, Auto Dealerships and Auto Body Shops

Industry/Entity Type

Auto Repair

Contact Information for Business Card

Dennis Holbrook
PO Box 538 Ashmere, NY 11952
631-472-8816
corvellapdr@mailnest.example
website corvellapdr.example
youtube corvella paintless dent removal
25 years of experience removing Dents, Dings and Hail Damage

Font styles to use
Serif
Sans Serif

Colors

Designer to choose colors to be used in the design.

Requirements
Must have
• I do like things that are simple but classy and somewhat bold, also I like my logo so that should be somewhat important

```html
<!DOCTYPE html>
<html lang="en">
<head>
<meta charset="utf-8">
<title>Corvella Paintless Dent Removal – Business Card</title>
<link rel="stylesheet" href="https://fonts.googleapis.com/css2?family=Arimo:wght@400;700&display=swap">
<style>
  :root {
    --backdrop: #3a3a3a;
    --card: #141414;
    --card-edge: #202020;
    --lime: #7cc520;
    --ink-light: #f2f2f2;
    --ink-dark: #1a2a10;
    --rule: #6a6a6a;
    --mark: #c9c9c9;
  }
  * { margin: 0; padding: 0; box-sizing: border-box; }
  html, body {
    width: 1200px; height: 900px; overflow: hidden;
    background: var(--backdrop);
    font-family: "Arimo", Arial, sans-serif;
  }
  .stage {
    width: 1200px; height: 900px;
    display: flex; align-items: center; justify-content: center; gap: 40px;
  }
  .card {
    position: relative;
    width: 540px; height: 310px;
    background: var(--card);
    border: 1px solid var(--card-edge);
    border-radius: 18px;
    overflow: hidden;
  }

  /* Wordmark */
  .wordmark {
    position: absolute;
    display: flex; align-items: center; gap: 10px;
    color: var(--mark);
    font-weight: 700;
    text-transform: uppercase;
    line-height: 1.15;
  }
  .wordmark-dot {
    width: 14px; height: 14px; border-radius: 50%;
    background: var(--mark); flex: none;
  }
  .wordmark-name { font-size: 26px; letter-spacing: 1px; display: block; }
  .wordmark-sub { font-size: 11px; letter-spacing: 0.5px; display: block; }

  /* Contact side */
  .card-contact .wordmark { left: 36px; top: 160px; color: var(--lime); }
  .card-contact .wordmark-dot { background: var(--lime); }
  .divider {
    position: absolute; left: 286px; top: 78px;
    width: 1px; height: 150px; background: var(--rule);
  }
  .contact {
    position: absolute; left: 300px; top: 58px;
    color: var(--ink-light); font-size: 13.5px; line-height: 1.45;
  }
  .contact-name {
    color: var(--lime); font-weight: 700; font-size: 18px;
    text-transform: uppercase; letter-spacing: 0.5px; margin-bottom: 4px;
  }
  .contact-line { display: flex; align-items: center; gap: 6px; }
  .contact-icon { width: 11px; height: 11px; flex: none; }
  .contact-address { margin-top: 2px; }
  .contact-label { color: var(--lime); }

  /* Tagline side */
  .card-tagline .wordmark { left: 50%; top: 78px; transform: translateX(-50%); white-space: nowrap; }
  .tagline-band {
    position: absolute; left: 0; right: 0; top: 180px; height: 38px;
    background: var(--lime);
    display: flex; align-items: center; justify-content: center;
    color: var(--ink-dark); font-weight: 700; font-size: 12.5px;
    text-transform: uppercase; letter-spacing: 0.3px;
  }
</style>
</head>
<body>
<main class="stage">

  <section class="card card-contact">
    <div class="wordmark">
      <span class="wordmark-dot"></span>
      <span>
        <span class="wordmark-name">Corvella</span>
        <span class="wordmark-sub">Paintless Dent Removal</span>
      </span>
    </div>
    <div class="divider"></div>
    <div class="contact">
      <div class="contact-name">Dennis Holbrook</div>
      <div class="contact-line">
        <svg class="contact-icon" viewBox="0 0 12 12"><path fill="#7cc520" d="M2.5 1h2l1 3-1.3 1a6 6 0 0 0 2.8 2.8l1-1.3 3 1v2a1.5 1.5 0 0 1-1.5 1.5A9 9 0 0 1 1 2.5 1.5 1.5 0 0 1 2.5 1z"/></svg>
        <span>631-472-8816</span>
      </div>
      <div class="contact-line">
        <svg class="contact-icon" viewBox="0 0 12 12"><rect x="0.5" y="2" width="11" height="8" rx="1" fill="#7cc520"/><path d="M1 3l5 4 5-4" fill="none" stroke="#141414" stroke-width="1.2"/></svg>
        <span>corvellapdr@mailnest.example</span>
      </div>
      <div class="contact-line">
        <svg class="contact-icon" viewBox="0 0 12 12"><circle cx="6" cy="6" r="5.5" fill="#7cc520"/><path d="M0.5 6h11M6 0.5c-2.5 3-2.5 8 0 11M6 0.5c2.5 3 2.5 8 0 11" fill="none" stroke="#141414" stroke-width="0.9"/></svg>
        <span>corvellapdr.example</span>
      </div>
      <div class="contact-address">PO Box 538 Ashmere,<br>NY 11952</div>
      <div class="contact-label">youtube:</div>
      <div>corvella paintless dent removal</div>
    </div>
  </section>

  <section class="card card-tagline">
    <div class="wordmark">
      <span class="wordmark-dot"></span>
      <span>
        <span class="wordmark-name">Corvella</span>
        <span class="wordmark-sub">Paintless Dent Removal</span>
      </span>
    </div>
    <div class="tagline-band">25 Years of Experience Removing Dents, Dings and Hail Damage</div>
  </section>

</main>
</body>
</html>
```